Pharma Business needs a new careers template

We need a new job posting template to use for all of our open positions. We are in the pharma production business and want to elevate our job postings. The design should incorporate our company colours (namely blue and white).<br/><br/>The completed work should look professional, innovative and slightly quirky.<br/><br/>Feel free to familiarise yourself with some of our current designs on our website (www.torvax.com).<br/><br/>We have a few ideas of how we want the template to look like:<br/><br/>- We would like the design to incorporate various boxes that show different information like "Role Profile", "Benefits" etc.<br/><br/>- We would like to show some of our achievements in a special type of ellipses that remind of tablets or capsules. See a close example of another job posting incorporating similar design (but with circles instead of capsules/tablets) attached.<br/><br/>- We would like some of the main information like job location, contact phone etc to be shown after a corresponding icon. Example screenshot applied.<br/><br/>We have also attached an example job posting to give you an idea of what information our template should hold.

Industry/Entity Type

Pharmaceutical

Colors
33a6d7
ffffff
0393ce
3277b5

Requirements
Must have
• The file should be editable so we can freely fill it for each new position. We should also have it in PSD format.

```html
<!DOCTYPE html>
<html lang="en">
<head>
<meta charset="utf-8">
<title>Torvax Pharma – Careers</title>
<link rel="stylesheet" href="https://fonts.googleapis.com/css2?family=Open+Sans:wght@400;600;700&display=swap">
<style>
  :root{
    --navy:#0c2b57;
    --deep:#0a3a72;
    --brand:#0a5595;
    --title:#0b4f8c;
    --accent:#3277b5;
    --sky:#33a6d7;
    --ink:#1b1b1b;
    --white:#ffffff;
    --stage:#e9eaec;
  }
  *{box-sizing:border-box;margin:0;padding:0}
  html,body{width:1200px;height:1200px;overflow:hidden;background:var(--stage)}
  body{position:relative;font-family:"Open Sans",Arial,sans-serif}
  .flyer{
    position:absolute;left:186px;top:15px;
    width:1152px;height:1627px;background:var(--white);
    transform:scale(.7191);transform-origin:top left;overflow:hidden;
  }
  .hero{position:absolute;left:0;top:0}
  .brand-name{
    position:absolute;left:880px;top:40px;width:220px;text-align:center;
    font-weight:700;font-size:36px;color:var(--deep);line-height:1.1;
  }
  .intro{
    position:absolute;left:52px;top:676px;width:488px;
    font-size:15px;font-weight:600;line-height:18.6px;color:var(--ink);text-align:justify;
  }
  .role-profile{
    position:absolute;left:0;top:888px;width:572px;height:374px;background:var(--brand);color:var(--white);
    padding:28px 30px 0 50px;
  }
  .role-profile .arrow{position:absolute;right:-34px;top:150px;width:0;height:0;
    border-top:36px solid transparent;border-bottom:36px solid transparent;border-left:34px solid var(--brand)}
  .box-title{display:flex;align-items:center;gap:16px;font-size:30px;font-weight:700;line-height:1}
  .box-title svg{flex:none}
  .rule{width:68px;height:3px;background:var(--white);margin:14px 0 16px}
  .role-profile p{font-size:19px;line-height:26.4px;letter-spacing:-.1px}
  .success{position:absolute;left:622px;top:870px;width:500px}
  .success h2{display:flex;gap:20px;align-items:flex-start;font-size:30px;line-height:27px;font-weight:700;color:var(--title)}
  .success h2 svg{margin-top:4px;flex:none}
  .checks{list-style:none;margin-top:18px}
  .checks li{display:flex;gap:10px;font-size:15px;font-weight:600;line-height:21px;color:var(--ink);margin-bottom:9px}
  .checks svg{flex:none;margin-top:3px}
  .challenge{position:absolute;left:48px;top:1280px;width:510px}
  .challenge h2{display:flex;gap:10px;align-items:center;font-size:22px;font-weight:700;color:var(--title);white-space:nowrap;letter-spacing:-.2px}
  .challenge h2 svg{flex:none}
  .challenge p{margin-top:16px;font-size:15.5px;line-height:22px;color:var(--ink);width:500px}
  .benefits{position:absolute;left:572px;top:1250px;width:580px;height:295px;background:var(--brand);color:var(--white);padding:18px 40px 0 40px}
  .benefits .rule{margin:10px 0 12px 48px}
  .benefits ul{list-style:none}
  .benefits li{position:relative;padding-left:36px;font-size:15px;font-weight:600;line-height:21px;margin-bottom:12px}
  .benefits li::before{content:"";position:absolute;left:6px;top:6px;width:9px;height:9px;background:var(--white);transform:rotate(45deg)}
  .contact{position:absolute;left:0;top:1545px;width:1152px;height:82px;background:var(--navy);color:var(--white);
    display:flex;align-items:center;justify-content:space-between;padding:0 45px 0 50px;font-size:32px}
  .contact span{display:flex;align-items:center;gap:22px}
  .contact .sep{width:2px;height:40px;background:var(--white)}
</style>
</head>
<body>
<div class="flyer">
  <svg class="hero" width="1152" height="860" viewBox="0 0 1152 860">
    <defs>
      <linearGradient id="shop" x1="0" y1="0" x2="1" y2="1">
        <stop offset="0" stop-color="#d9dde3"/><stop offset=".5" stop-color="#c9d4e2"/><stop offset="1" stop-color="#e8eef5"/>
      </linearGradient>
      <radialGradient id="pills" cx=".5" cy=".55" r=".6">
        <stop offset="0" stop-color="#f2efe9"/><stop offset=".6" stop-color="#e9c98a"/><stop offset="1" stop-color="#f4f3f1"/>
      </radialGradient>
    </defs>
    <path role="img" aria-label="Photo of a pharmacist advising a customer in a pharmacy aisle" fill="url(#shop)"
      d="M0 0H780C800 120 900 190 1040 190C1100 190 1140 170 1152 160V440C1000 570 800 630 500 640C300 645 120 590 0 515Z"/>
    <path d="M0 515C120 590 300 645 500 640C800 630 1000 570 1152 440" fill="none" stroke="var(--deep)" stroke-width="22"/>
    <path d="M780 0C800 120 900 190 1040 190C1100 190 1140 170 1152 160" fill="none" stroke="var(--deep)" stroke-width="12"/>
    <path d="M770 0C785 140 900 200 1040 198" fill="none" stroke="var(--accent)" stroke-width="4"/>
    <circle cx="863" cy="658" r="186" fill="var(--navy)"/>
    <circle role="img" aria-label="Photo of colourful capsules and tablets" cx="863" cy="658" r="168" fill="url(#pills)"/>
    <ellipse cx="863" cy="848" rx="170" ry="5" fill="#b9bfc8"/>
  </svg>
  <div class="brand-name">Torvax<br>Pharma</div>

  <p class="intro">Habitasse Porta Luctus Porta. Aptent Augue. Justo Aliquet Urna Justo. Inceptos Ligula Elit Aenean Maecenas Montes Ullamcorper Commodo Volutpat Massa Aliquam Velit Interdum Viverra Congue Malesuada Lacus Lobortis Egestas Malesuada Blandit Nec Facilisis.fermentum Tempor Arcu Litora Fringilla, Quis Aenean Sagittis Feugiat A Pretium Hendrerit Sociosqu Mattis, Maecenas. Turpis Lorem. Aliquet Nibh Sociis Mus Facilisi Interdum Aliquet Aenean Sem Vulputate Natoque. Malesuada Rutrum Sociosqu Sociosqu Litora Nunc Ornare Feugiat Volutpat Feugiat Natoque Dictumst Scelerisque Sociis Ornare Eget Inceptos Quam Interdum.</p>

  <section class="role-profile">
    <div class="box-title">
      <svg width="36" height="36" viewBox="0 0 36 36"><circle cx="18" cy="18" r="16" fill="none" stroke="#fff" stroke-width="3"/><circle cx="18" cy="14" r="6" fill="#fff"/><path d="M7 29c3-6 8-7 11-7s8 1 11 7" fill="#fff"/></svg>
      ROLE PROFILE:
    </div>
    <div class="rule"></div>
    <p>Velit Commodo, Ultrices Proin Tellus Montes Magnis Mi Porttitor Metus Sociis Condimentum Dis Platea. Ad Consectetuer Laoreet Euismod Ad Donec Tellus Elit Ad Metus Lectus. Sit Pretium Quis Imperdiet Velit Turpis Diam Urna Torquent Ante Phasellus Nascetur Per Euismod Ultrices Consectetuer A.Sollicitudin Lobortis Scelerisque Vel Senectus Id, Pharetra Iaculis NonSem Id Nam Odio Fames Facilisi Quam Integer Condimentum Rutrum Pulvinar Inceptos. Montes Id Nonummy Platea, Mattis Proin Cum.</p>
    <div class="arrow"></div>
  </section>

  <section class="success">
    <h2>
      <svg width="38" height="38" viewBox="0 0 38 38"><circle cx="19" cy="19" r="19" fill="var(--title)"/><path d="M11 22l5 5 11-13" fill="none" stroke="#fff" stroke-width="3"/></svg>
      <span>To Be Successful In This Role You Should Have:</span>
    </h2>
    <ul class="checks">
      <li><svg width="16" height="16" viewBox="0 0 16 16"><circle cx="8" cy="8" r="6.5" fill="none" stroke="var(--accent)" stroke-width="1.5"/><path d="M5 8l2 2 5-6" fill="none" stroke="var(--accent)" stroke-width="1.6"/></svg>Cubilia. Porta. Morbi Aliquet Aptent Aenean Nostra Purus.</li>
      <li><svg width="16" height="16" viewBox="0 0 16 16"><circle cx="8" cy="8" r="6.5" fill="none" stroke="var(--accent)" stroke-width="1.5"/><path d="M5 8l2 2 5-6" fill="none" stroke="var(--accent)" stroke-width="1.6"/></svg>Rhoncus Vitae Mus Fermentum Placerat Placerat Libero.</li>
      <li><svg width="16" height="16" viewBox="0 0 16 16"><circle cx="8" cy="8" r="6.5" fill="none" stroke="var(--accent)" stroke-width="1.5"/><path d="M5 8l2 2 5-6" fill="none" stroke="var(--accent)" stroke-width="1.6"/></svg>Interdum, Dapibus Aliquet Dignissim Hac Fusce Non. Consectetuer.</li>
      <li><svg width="16" height="16" viewBox="0 0 16 16"><circle cx="8" cy="8" r="6.5" fill="none" stroke="var(--accent)" stroke-width="1.5"/><path d="M5 8l2 2 5-6" fill="none" stroke="var(--accent)" stroke-width="1.6"/></svg>Quam Hac, Ornare Hendrerit Ultricies.</li>
      <li><svg width="16" height="16" viewBox="0 0 16 16"><circle cx="8" cy="8" r="6.5" fill="none" stroke="var(--accent)" stroke-width="1.5"/><path d="M5 8l2 2 5-6" fill="none" stroke="var(--accent)" stroke-width="1.6"/></svg>Netus Parturient Elementum, Nisi Purus Dui.</li>
      <li><svg width="16" height="16" viewBox="0 0 16 16"><circle cx="8" cy="8" r="6.5" fill="none" stroke="var(--accent)" stroke-width="1.5"/><path d="M5 8l2 2 5-6" fill="none" stroke="var(--accent)" stroke-width="1.6"/></svg>Justo Sodales, Suspendisse Fermentum, Quisque Fermentum Quisque Pulvinar.</li>
      <li><svg width="16" height="16" viewBox="0 0 16 16"><circle cx="8" cy="8" r="6.5" fill="none" stroke="var(--accent)" stroke-width="1.5"/><path d="M5 8l2 2 5-6" fill="none" stroke="var(--accent)" stroke-width="1.6"/></svg>Convallis Lectus Feugiat Suspendisse Ullamcorper Nonummy Duis Pretium.</li>
      <li><svg width="16" height="16" viewBox="0 0 16 16"><circle cx="8" cy="8" r="6.5" fill="none" stroke="var(--accent)" stroke-width="1.5"/><path d="M5 8l2 2 5-6" fill="none" stroke="var(--accent)" stroke-width="1.6"/></svg>Eget Pretium Per Tempor Natoque. Quisque.</li>
    </ul>
  </section>

  <section class="challenge">
    <h2>
      <svg width="32" height="32" viewBox="0 0 32 32"><circle cx="16" cy="16" r="16" fill="var(--title)"/><circle cx="16" cy="16" r="9" fill="none" stroke="#fff" stroke-width="2"/><circle cx="16" cy="16" r="3" fill="#fff"/></svg>
      Challenged By This Career Opportunity?
    </h2>
    <p>Curae; Eros Cubilia Suspendisse Netus Turpis Laoreet Nonummy Vivamus Scelerisque Rutrum.<br>Risus Porttitor Semper Erat Lorem Ante Orci Cum Natoque Mauris Lobortis. Velit Semper Aliquet.metus Proin Ullamcorper Augue Urna. Eros Taciti Maecenas Est, Aliquam Parturient Etiam Gravida Nullam Molestie. Sem Imperdiet.<br>Porta Praesent Sit. Vitae Pede Luctus Et Potenti Ac Augue Primis Cum Vel. Blandit Scelerisque Tincidunt Tincidunt Luctus Pretium Eleifend.</p>
  </section>

  <section class="benefits">
    <div class="box-title">
      <svg width="34" height="34" viewBox="0 0 34 34"><circle cx="17" cy="17" r="17" fill="#fff"/><rect x="9" y="17" width="4" height="9" fill="var(--brand)"/><rect x="15" y="12" width="4" height="14" fill="var(--brand)"/><rect x="21" y="14" width="4" height="12" fill="var(--brand)"/></svg>
      BENIFIT
    </div>
    <div class="rule"></div>
    <ul>
      <li>Nonummy fermentum nec dictumst et.</li>
      <li>Venenatis. Aenean ac. Commodo volutpat dolor libero mus.</li>
      <li>Cras consequat, non tempor justo.</li>
      <li>Natoque potenti Hymenaeos ad tristique torquent ultrices. Nec donec. Eu.</li>
      <li>Ac consequat ridiculus convallis curae; porttitor.</li>
      <li>Lobortis non hendrerit taciti sed. Cursus.</li>
    </ul>
  </section>

  <footer class="contact">
    <span><svg width="26" height="20" viewBox="0 0 26 20"><rect width="26" height="20" fill="#fff"/><path d="M1 1l12 10L25 1" fill="none" stroke="var(--navy)" stroke-width="2.5"/></svg>jobs@torvax.com</span>
    <i class="sep"></i>
    <span><svg width="24" height="24" viewBox="0 0 24 24"><path d="M5 2l4 1 1 5-3 2c1 3 3 5 6 6l2-3 5 1 1 4-3 3C10 21 3 14 2 5z" fill="#fff"/></svg>555-010-0000</span>
    <i class="sep"></i>
    <span><svg width="26" height="26" viewBox="0 0 26 26" fill="none" stroke="#fff" stroke-width="2"><circle cx="13" cy="13" r="11"/><ellipse cx="13" cy="13" rx="5" ry="11"/><path d="M2 13h22M4 7h18M4 19h18"/></svg>www.torvax.com</span>
  </footer>
</div>
</body>
</html>
```